Studying Effectively To Do List

I am looking to design a new "Study To Do List" for High School students (Ages 15 - 18) . This will be printed as an A4 notepad and so should only be a single A4 page.

The Design will need to be professional and look semi-serious but also be appealing to High school students (Ages 15 - 18) and should NOT be gender specific.

I have attached a word document outlining the structure of the page. The space provided should be large enough that people can write in it comfortably.

The notepad will most likely be printed in black and white but I'm also looking at coloured options - colours should be kept to a minimum.

This will be printed professionally and should also include a 3mm bleed.

The design should also include the business logo (included in the word document)

Target Market(s)

High School students (Ages 15 - 18). Both genders

Industry/Entity Type

Education

Font styles to use
Serif
Sans Serif

Requirements
Must have
• Please see the word document attached.
Should not have
• Too much colour

```html
<!DOCTYPE html>
<html lang="en">
<head>
<meta charset="utf-8">
<title>Study To Do List</title>
<link href="https://fonts.googleapis.com/css2?family=Lato:wght@400;700&display=swap" rel="stylesheet">
<style>
:root{
  --navy:#1f3346;
  --orange:#f47a20;
  --field-a:#e9eaec;
  --field-b:#f4f5f7;
  --paper:#ffffff;
  --backdrop:#a5a6a8;
}
*{box-sizing:border-box;margin:0;padding:0}
html,body{width:1200px;height:1200px;overflow:hidden;background:var(--backdrop);font-family:'Lato',sans-serif;color:var(--navy)}
.sheet-frame{position:absolute;left:190px;top:19px;width:728px;height:1031px;transform:scale(1.1264);transform-origin:0 0}
.sheet{position:relative;width:728px;height:1031px;background:var(--paper)}
.brand{position:absolute;left:270px;top:46px;width:200px;display:flex;align-items:center;gap:8px}
.brand-dot{width:16px;height:16px;border-radius:50%;background:var(--orange);flex:none}
.brand-name{font-size:17px;font-weight:700;color:var(--navy);white-space:nowrap}
.date{position:absolute;left:519px;top:72px;font-size:14px}
.date-line{display:inline-block;width:126px;border-bottom:1px dotted var(--navy);margin-left:3px}
.section-tab{position:absolute;left:44px;height:17px;background:var(--navy);color:#fff;font-size:14px;line-height:18px;padding-left:7px;clip-path:polygon(0 0,calc(100% - 17px) 0,100% 100%,0 100%)}
.grid{position:absolute;left:44px;width:641px;border-collapse:collapse;table-layout:fixed;font-size:14px;border:2px solid var(--navy)}
.grid td{border:1px solid var(--navy);padding:0 6px;white-space:nowrap}
.grid .label{background:#fff}
.grid .field{background:var(--field-b)}
.grid .field.shade{background:var(--field-a)}
.grid .num{background:#fff;padding-left:7px}
.revision{top:138px;height:89px}
.revision tr{height:22px}
.homework{top:256px;height:283px}
.assessments{top:568px;height:283px}
.assessments .label{padding-left:10px}
.assessments .due{padding-left:16px;background:#fff}
.tracker{position:absolute;left:44px;top:867px;width:641px;border-collapse:collapse;table-layout:fixed;font-size:14px;border:1px solid var(--navy)}
.tracker th{background:var(--navy);color:#fff;font-weight:400;height:22px;border-left:1px solid #fff}
.tracker td{border:1px solid var(--navy);height:23px;background:#fff;padding-left:7px}
.footer-band{position:absolute;left:0;top:1004px;width:728px;height:15px;background:var(--orange);color:#fff;font-size:13px;line-height:15px;text-align:center}
</style>
</head>
<body>
<div class="sheet-frame">
  <div class="sheet">
    <div class="brand"><span class="brand-dot"></span><span class="brand-name">Northpath Study</span></div>
    <div class="date">Date: <span class="date-line"></span></div>

    <div class="section-tab" style="top:121px;width:97px">REVISION</div>
    <table class="grid revision">
      <colgroup><col style="width:26px"><col style="width:292px"><col style="width:24px"><col></colgroup>
      <tr><td class="num">1</td><td class="field shade"></td><td class="num">5</td><td class="field shade"></td></tr>
      <tr><td class="num">2</td><td class="field"></td><td class="num">6</td><td class="field"></td></tr>
      <tr><td class="num">3</td><td class="field shade"></td><td class="num">7</td><td class="field shade"></td></tr>
      <tr><td class="num">4</td><td class="field"></td><td class="num">8</td><td class="field"></td></tr>
    </table>

    <div class="section-tab" style="top:240px;width:127px">HOMEWORK</div>
    <table class="grid homework">
      <colgroup><col style="width:73px"><col></colgroup>
      <tr><td class="label">Subject</td><td class="field shade"></td></tr>
      <tr><td class="label">Task</td><td class="field"></td></tr>
      <tr><td class="label">Subject</td><td class="field shade"></td></tr>
      <tr><td class="label">Task</td><td class="field"></td></tr>
      <tr><td class="label">Subject</td><td class="field shade"></td></tr>
      <tr><td class="label">Task</td><td class="field"></td></tr>
      <tr><td class="label">Subject</td><td class="field shade"></td></tr>
      <tr><td class="label">Task</td><td class="field"></td></tr>
      <tr><td class="label">Subject</td><td class="field shade"></td></tr>
      <tr><td class="label">Task</td><td class="field"></td></tr>
      <tr><td class="label">Subject</td><td class="field shade"></td></tr>
      <tr><td class="label">Task</td><td class="field"></td></tr>
    </table>

    <div class="section-tab" style="top:552px;width:135px;padding-left:13px">ASSESSMENTS</div>
    <table class="grid assessments">
      <colgroup><col style="width:103px"><col style="width:217px"><col style="width:60px"><col></colgroup>
      <tr><td class="label">Assessment</td><td class="field shade"></td><td class="due">Due</td><td class="field shade"></td></tr>
      <tr><td class="label">Element</td><td class="field"></td><td class="due">Due</td><td class="field"></td></tr>
      <tr><td class="label">Assessment</td><td class="field shade"></td><td class="due">Due</td><td class="field shade"></td></tr>
      <tr><td class="label">Element</td><td class="field"></td><td class="due">Due</td><td class="field"></td></tr>
      <tr><td class="label">Assessment</td><td class="field shade"></td><td class="due">Due</td><td class="field shade"></td></tr>
      <tr><td class="label">Element</td><td class="field"></td><td class="due">Due</td><td class="field"></td></tr>
      <tr><td class="label">Assessment</td><td class="field shade"></td><td class="due">Due</td><td class="field shade"></td></tr>
      <tr><td class="label">Element</td><td class="field"></td><td class="due">Due</td><td class="field"></td></tr>
      <tr><td class="label">Assessment</td><td class="field shade"></td><td class="due">Due</td><td class="field shade"></td></tr>
      <tr><td class="label">Element</td><td class="field"></td><td class="due">Due</td><td class="field"></td></tr>
      <tr><td class="label">Assessment</td><td class="field shade"></td><td class="due">Due</td><td class="field shade"></td></tr>
      <tr><td class="label">Element</td><td class="field" colspan="3"></td></tr>
    </table>

    <table class="tracker">
      <colgroup><col style="width:23px"><col style="width:123px"><col style="width:24px"><col style="width:114px"><col style="width:25px"><col></colgroup>
      <tr><th colspan="4" style="border-left:none">NOTES</th><th></th><th>PRACTICE</th></tr>
      <tr><td>1</td><td></td><td>5</td><td></td><td>1</td><td></td></tr>
      <tr><td>2</td><td></td><td>6</td><td></td><td>2</td><td></td></tr>
      <tr><td>3</td><td></td><td>7</td><td></td><td>3</td><td></td></tr>
      <tr><td>4</td><td></td><td>8</td><td></td><td>4</td><td></td></tr>
    </table>

    <div class="footer-band">northpathstudy.com.au</div>
  </div>
</div>
</body>
</html>
```